maple crest homeworks KOVA

Looking for business card design that represents our company. we are maple crest homeworks and we dedicate our skills of home energy efficiency to our customer by providing energy solution to their energy problems.
HVAC
SOLAR
INSULLATION
LIGHTING
DUCT TESTING
KOVA RATING.

```html
<!DOCTYPE html>
<html lang="en">
<head>
<meta charset="utf-8">
<title>Maple Crest Homeworks – Business Card</title>
<link rel="stylesheet" href="https://fonts.googleapis.com/css2?family=Questrial&family=Montserrat:wght@600;700&family=Arimo:wght@400&display=swap">
<style>
  :root {
    --stage: #1e1e1e;
    --card: #141414;
    --card-edge: #1b1b1b;
    --green: #8cc63f;
    --blue: #29a8e0;
    --white: #f2f2f2;
    --rule: #d8d8d8;
  }
  * { box-sizing: border-box; margin: 0; padding: 0; }
  html, body {
    width: 1200px; height: 1200px; overflow: hidden;
    background: radial-gradient(circle at 60% 30%, #2a2a2a 0%, var(--stage) 60%, #151515 100%);
  }
  .stage {
    position: relative; width: 1200px; height: 1200px;
    display: flex; flex-direction: column; align-items: center; justify-content: center; gap: 56px;
  }
  .card {
    position: relative; width: 840px; height: 480px;
    background: linear-gradient(160deg, var(--card-edge), var(--card));
    border-radius: 22px;
    box-shadow: 0 18px 40px rgba(0,0,0,.55);
    overflow: hidden;
  }
  .brand {
    position: absolute; left: 0; right: 0;
    display: flex; align-items: center; justify-content: center; gap: 16px;
  }
  .brand-dot {
    width: 34px; height: 34px; border-radius: 50%; background: var(--blue); flex: none;
  }
  .brand-name {
    font-family: "Questrial", sans-serif; font-size: 44px; letter-spacing: 2px;
    color: var(--green); text-transform: uppercase; white-space: nowrap;
  }
  .card--front .brand { top: 170px; }
  .services {
    position: absolute; left: 0; right: 0; bottom: 58px;
    display: flex; justify-content: center; align-items: center; gap: 12px;
    font-family: "Montserrat", sans-serif; font-weight: 700; font-size: 17px;
    color: var(--green); letter-spacing: .5px; white-space: nowrap;
  }
  .services .sep {
    width: 9px; height: 9px; border-radius: 50%; background: var(--blue); flex: none;
  }
  .card--back .brand { top: 100px; }
  .person { position: absolute; left: 70px; top: 262px; }
  .person-name {
    font-family: "Questrial", sans-serif; font-size: 40px; color: var(--green); line-height: 1;
  }
  .person-role {
    font-family: "Questrial", sans-serif; font-size: 25px; color: var(--blue); margin-top: 4px;
  }
  .person-address {
    font-family: "Arimo", sans-serif; font-size: 19px; color: var(--white); line-height: 1.35; margin-top: 8px;
  }
  .rule {
    position: absolute; left: 400px; right: 60px; top: 350px; height: 1px; background: var(--rule);
  }
  .contacts {
    position: absolute; right: 60px; top: 372px;
    display: flex; flex-direction: column; align-items: flex-end; gap: 6px;
    font-family: "Arimo", sans-serif; font-size: 19px; color: var(--white);
  }
  .contact { display: flex; align-items: center; gap: 12px; }
  .contact svg { width: 22px; height: 22px; flex: none; }
</style>
</head>
<body>
<main class="stage">
  <section class="card card--front">
    <div class="brand">
      <span class="brand-dot"></span>
      <span class="brand-name">Maple Crest Homeworks</span>
    </div>
    <div class="services">
      <span>HVAC</span><span class="sep"></span>
      <span>SOLAR</span><span class="sep"></span>
      <span>INSULLATION</span><span class="sep"></span>
      <span>LIGHTING</span><span class="sep"></span>
      <span>DUCT TESTING</span><span class="sep"></span>
      <span>KOVA RATING.</span>
    </div>
  </section>

  <section class="card card--back">
    <div class="brand">
      <span class="brand-dot"></span>
      <span class="brand-name">Maple Crest Homeworks</span>
    </div>
    <div class="person">
      <p class="person-name">Daniel Harlow</p>
      <p class="person-role">Managing Director</p>
      <p class="person-address">214 Alder Bay Road<br>Kelowna Canada</p>
    </div>
    <div class="rule"></div>
    <div class="contacts">
      <div class="contact">
        <span>028-317-0962</span>
        <svg viewBox="0 0 24 24" aria-hidden="true"><path fill="var(--blue)" d="M6.6 10.8a15 15 0 0 0 6.6 6.6l2.2-2.2c.3-.3.7-.4 1-.2 1.1.4 2.3.6 3.6.6.6 0 1 .4 1 1V20c0 .6-.4 1-1 1A17 17 0 0 1 3 4c0-.6.4-1 1-1h3.5c.6 0 1 .4 1 1 0 1.3.2 2.5.6 3.6.1.3 0 .7-.2 1z"/></svg>
      </div>
      <div class="contact">
        <span>danielharlow@maplecresthomeworks.com</span>
        <svg viewBox="0 0 24 24" aria-hidden="true"><rect x="2" y="5" width="20" height="14" rx="1.5" fill="var(--blue)"/><path d="M3 6l9 7 9-7" fill="none" stroke="var(--card)" stroke-width="1.6"/></svg>
      </div>
      <div class="contact">
        <span>www.maplecresthomeworks.com</span>
        <svg viewBox="0 0 24 24" aria-hidden="true"><g fill="none" stroke="var(--blue)" stroke-width="1.7"><circle cx="12" cy="12" r="9"/><ellipse cx="12" cy="12" rx="4" ry="9"/><path d="M3 12h18M4.5 7.5h15M4.5 16.5h15"/></g></svg>
      </div>
    </div>
  </section>
</main>
</body>
</html>
```